Electrical Industry Newletter Design Project PSD format with layers

The Name of the newsletter is:
A "Pulse" of the Hour
-This is a bi monthly newsletter focused on the Electrical and Cabling Industry
"Pulse" of course is a play on words referring to a Sine wave
We are looking for a creative yet professional looking newsletter. Our targeted audience are professional consulting engineers, architects, & property owners/manager.
We are looking for a unique logo for the newsletters name "Pull of the Hours" with the subtext being "Electrical & Cabling Industry"
We envision the incorporations of the sin wave into the logo and other such associated symbols associated with our industry.
Note: the Newsletter is going to be brought to them by our company KAV Electric. Our logo should be incorporated near the top of the newsletter but be less prominent.
Each issue is going to be a "Vol" Hence the Vol number should be editable.
There should be a featured article area labeled
-Whats Happening
-This section should have a spot for a relevant pictures
There should be a side section labeled
-Code Alert!
-Just for laughs
-This section should be available to place a relevant picture or comic strips of sorts.
The should be a section labeled
-Project Profile (This will be where we profile a recent project with pictures
You have total artistic license with this project, I know you will produce a great work of art!
Updates
What happened to all those creative juices??? Added Thursday, April 27, 2017
Target Market(s)
Consulting Engineers, Architects, Specifiers, Building Owners & Managers
Industry/Entity Type
Electrical
Look and feel

```html
<!DOCTYPE html>
<html lang="en">
<head>
<meta charset="utf-8">
<title>A "Pulse" of the Hour – Newsletter</title>
<link href="https://fonts.googleapis.com/css2?family=Fira+Sans:wght@300;400;500;600;700&display=swap" rel="stylesheet">
<style>
:root{
  --page:#e0e0e0;
  --sheet:#f4f4f4;
  --red:#d4102b;
  --ink:#444;
  --muted:#555;
  --soft:#888;
  --line:#cfcfcf;
  --navy:#2f3241;
  --hero-a:#3f3b45;
  --hero-b:#5a5560;
  --link:#1f5fb4;
  --white:#fff;
  --ornament:#d2d2d2;
}
*{margin:0;padding:0;box-sizing:border-box}
html,body{width:1200px;height:2384px;overflow:hidden;background:var(--page);font-family:"Fira Sans",Arial,sans-serif;color:var(--ink)}
.stage{position:relative;width:1200px;height:2384px}
.abs{position:absolute}
.contact-note{left:0;width:1200px;top:56px;text-align:center;font-size:20px;color:#222}
.contact-note a{color:var(--link);text-decoration:underline}
.sheet{left:226px;top:95px;width:750px;height:2136px;background:var(--sheet);border-top:5px solid var(--red);box-shadow:0 22px 18px -16px rgba(0,0,0,.35)}
.masthead-title{left:0;width:1200px;top:120px;text-align:center;font-size:44px;font-weight:300;color:var(--red)}
.masthead-sub{left:0;width:1200px;top:175px;text-align:center;font-size:20px;font-weight:600;color:#222}
.title-ornament{top:122px;width:136px;height:48px;border-radius:24px;background:linear-gradient(90deg,rgba(210,210,210,.15),var(--ornament) 50%,rgba(210,210,210,.15))}
.company-mark{left:0;width:1200px;top:226px;display:flex;justify-content:center;align-items:center;gap:10px;font-size:18px;font-weight:600;letter-spacing:2px;color:#222}
.company-mark i{display:block;width:20px;height:20px;background:#222}
.hero{left:257px;top:286px;width:692px;height:319px;background:linear-gradient(110deg,var(--hero-b),var(--hero-a) 60%,#4b4752)}
.hero-greet{left:291px;top:400px;font-size:38px;font-weight:300;color:var(--white)}
.hero-name{left:291px;top:448px;font-size:19px;font-weight:600;color:var(--white)}
.hero-btn{left:292px;top:499px;width:162px;height:62px;border:1.5px solid var(--white);color:var(--white);font-size:18px;font-weight:600;display:flex;align-items:center;justify-content:center;gap:6px}
.hero-map{left:257px;top:286px;width:692px;height:319px}
.intro{left:262px;top:634px;width:680px;font-size:17.5px;line-height:26px;color:var(--muted)}
.section-label{font-size:17px;font-weight:600;letter-spacing:.5px;color:var(--muted);text-align:center}
.rule{height:1.5px;background:var(--line)}
.article-title{font-size:24px;font-weight:400;color:var(--ink)}
.title-rule{height:1.5px;width:138px;background:var(--line)}
.thumb{width:190px;height:190px;border-radius:50%;overflow:hidden}
.date-badge{left:46px;top:96px;width:104px;height:60px;background:var(--red);clip-path:polygon(0 30%,100% 0,100% 100%,0 100%);color:var(--white);font-size:22px;display:flex;align-items:flex-end;justify-content:center;padding-bottom:8px}
.excerpt{width:296px;font-size:17.5px;line-height:27.5px;color:var(--muted)}
.read-more{font-size:17px;font-weight:600;color:var(--red)}
.see-more{left:440px;top:1452px;width:150px;height:59px;border:2px solid var(--line);color:var(--soft);font-size:17px;display:flex;align-items:center;justify-content:center;gap:6px}
.code-alert{left:775px;top:869px;width:170px;height:200px;background:var(--navy);color:var(--white);font-size:17.5px;display:flex;align-items:center;justify-content:center}
.comic{left:775px;width:170px}
.photo{top:1689px}
.footer{left:259px;top:1993px;width:686px;height:205px;background:var(--white);border:1.5px solid #e4e4e4}
.footer-line{left:324px;font-size:16px;color:#444;line-height:26px}
.footer-icon{left:288px;width:22px;height:22px}
.social{top:2077px;width:32px;height:32px;border:2px solid #555;border-radius:50%}
.copyright{left:600px;width:314px;top:2126px;text-align:right;font-size:17px;font-weight:600;color:var(--muted)}
</style>
</head>
<body>
<div class="stage">

  <p class="abs contact-note">For anything about this mail you can contract us by <a href="#">CLICK THIS LINK.</a></p>

  <div class="abs sheet"></div>

  <div class="abs title-ornament" style="left:262px" role="img" aria-label="Decorative grey wave ornament left of the title"></div>
  <div class="abs title-ornament" style="left:810px" role="img" aria-label="Decorative grey wave ornament right of the title"></div>

  <h1 class="abs masthead-title">A "Pulse" of the Hour</h1>
  <p class="abs masthead-sub">Electrical &amp; Cabling Industry"</p>
  <div class="abs company-mark"><i></i><span>KAV ELECTRIC LLC</span></div>

  <div class="abs hero" role="img" aria-label="Close-up photograph of bundled electrical cables with exposed copper cores"></div>
  <p class="abs hero-greet">Wellcome to</p>
  <p class="abs hero-name">A Pulse of the Hour</p>
  <div class="abs hero-btn">See More <svg width="10" height="14" viewBox="0 0 10 14"><path d="M2 2l5 5-5 5" fill="none" stroke="#fff" stroke-width="2.5"/></svg></div>

  <svg class="abs hero-map" viewBox="0 0 692 319" font-family="Fira Sans, Arial, sans-serif">
    <g fill="none" stroke="#fff" stroke-width="2" stroke-dasharray="2 5">
      <path d="M480 105 Q 520 70 545 80"/>
      <path d="M440 205 Q 450 245 500 250"/>
      <path d="M610 150 Q 630 175 600 190"/>
    </g>
    <circle cx="573" cy="94" r="63" fill="var(--red)"/>
    <circle cx="579" cy="91" r="61" fill="#fff"/>
    <circle cx="430" cy="145" r="63" fill="var(--red)"/>
    <circle cx="436" cy="140" r="61" fill="#fff"/>
    <circle cx="556" cy="239" r="63" fill="var(--red)"/>
    <circle cx="550" cy="234" r="61" fill="#fff"/>
    <g fill="#444" text-anchor="middle">
      <text x="579" y="97" font-size="17">Architects</text>
      <text x="436" y="136" font-size="17">Consulting</text>
      <text x="436" y="157" font-size="17">Engineers</text>
      <text x="550" y="231" font-size="17">property</text>
      <text x="550" y="250" font-size="12">owners/manager</text>
    </g>
  </svg>

  <p class="abs intro">With over two decades of combined experience in the electrical contracting and cabling industry, KAV Electric has earned a reputation all its own. Our commitment to the highest standards and customer satisfaction has always been our guiding principle.</p>

  <svg class="abs" style="left:524px;top:762px" width="42" height="40" viewBox="0 0 42 40" aria-hidden="true"><g fill="none" stroke="#666" stroke-width="2"><path d="M3 8h24v30H3z"/><path d="M8 14h6v12H8zM17 16h6M17 22h6M8 31h15"/><path d="M34 2v12M28 8h12"/></g></svg>
  <p class="abs section-label" style="left:257px;width:514px;top:814px">FEATURED ARTICLE</p>
  <div class="abs rule" style="left:257px;top:847px;width:514px"></div>

  <h2 class="abs article-title" style="left:262px;top:892px">Electrical Contracting</h2>
  <div class="abs title-rule" style="left:262px;top:926px"></div>
  <div class="abs thumb" style="left:258px;top:943px">
    <div style="width:100%;height:100%;background:linear-gradient(135deg,#6b7078,#b9bcc0 55%,#5a5e66)" role="img" aria-label="Photograph of electrical meter panels"></div>
    <div class="abs date-badge">30 April</div>
  </div>
  <p class="abs excerpt" style="left:472px;top:932px">Have a project you want us to look at? Whether you're in the predesign phase or ready to issue your project out to bid; we would welcome the opportunity to speak with ...</p>
  <p class="abs read-more" style="left:472px;top:1082px">Read More »</p>

  <h2 class="abs article-title" style="left:257px;top:1186px">Data and Telecommunication</h2>
  <div class="abs title-rule" style="left:258px;top:1220px"></div>
  <div class="abs thumb" style="left:258px;top:1240px">
    <div style="width:100%;height:100%;background:linear-gradient(135deg,#c9cdd2,#3f63b8 45%,#e0b32a 80%)" role="img" aria-label="Photograph of network patch cables"></div>
    <div class="abs date-badge">30 April</div>
  </div>
  <p class="abs excerpt" style="left:472px;top:1246px">As more work is being conducted online and in the cloud, the demand placed on existing communication networks is constantly being pushed to its limits. Words such as....</p>
  <p class="abs read-more" style="left:472px;top:1400px">Read More »</p>

  <div class="abs see-more">See more <svg width="9" height="12" viewBox="0 0 9 12"><path d="M2 2l4 4-4 4" fill="none" stroke="#888" stroke-width="2"/></svg></div>

  <div class="abs code-alert">Code Alert!</div>
  <div class="abs comic" style="top:1077px;height:216px;background:linear-gradient(160deg,#7fb7c9,#cfe0c0 55%,#8a9a5a)" role="img" aria-label="Comic strip panel for the Just for laughs section"></div>
  <div class="abs comic" style="top:1293px;height:220px;background:linear-gradient(170deg,#e8ecef,#8cc0dc 60%,#d8b640)" role="img" aria-label="Comic strip panel of a rider on horseback"></div>

  <svg class="abs" style="left:580px;top:1580px" width="38" height="38" viewBox="0 0 38 38" aria-hidden="true"><g fill="none" stroke="#666" stroke-width="2"><path d="M8 3h26v32H8z"/><path d="M3 9v26h5"/><path d="M13 10h16M13 16h16M13 22h16M13 28h16"/></g></svg>
  <p class="abs section-label" style="left:257px;width:688px;top:1626px">PROJECT PROFILE</p>
  <div class="abs rule" style="left:257px;top:1664px;width:688px"></div>

  <div class="abs photo" style="left:264px;width:407px;height:264px;background:linear-gradient(100deg,#d9d5cc,#eeeeec 50%,#b9bcbf)" role="img" aria-label="Photograph of an electrician in a yellow hard hat working on a panel"></div>
  <div class="abs photo" style="left:680px;width:137px;height:264px;background:linear-gradient(180deg,#9aa3a6,#b06a2c 55%,#6a5a40)" role="img" aria-label="Photograph of a worker in a safety harness on site"></div>
  <div class="abs photo" style="left:825px;width:119px;height:132px;background:linear-gradient(160deg,#2b3444,#7a8aa0 50%,#1e2530)" role="img" aria-label="Photograph of rows of cable terminations"></div>
  <div class="abs" style="left:825px;top:1832px;width:119px;height:121px;background:linear-gradient(160deg,#3a3f48,#aeb3ba 50%,#2c3038)" role="img" aria-label="Photograph of circuit breaker rows"></div>

  <div class="abs footer"></div>
  <svg class="abs footer-icon" style="top:2027px" viewBox="0 0 22 22" aria-hidden="true"><path d="M5 2l4 4-2 3c1 3 3 5 6 6l3-2 4 4-3 3C9 20 2 13 2 5z" fill="#555"/></svg>
  <p class="abs footer-line" style="top:2016px">555-014-2290</p>
  <svg class="abs footer-icon" style="top:2057px" viewBox="0 0 22 22" aria-hidden="true"><g fill="none" stroke="#777" stroke-width="1.6"><path d="M2 5h18v13H2z"/><path d="M2 5l9 7 9-7"/></g></svg>
  <p class="abs footer-line" style="top:2056px">info@kavelectric-mail.com</p>
  <svg class="abs footer-icon" style="top:2098px" viewBox="0 0 22 22" aria-hidden="true"><path d="M11 1a7 7 0 0 1 7 7c0 5-7 13-7 13S4 13 4 8a7 7 0 0 1 7-7z" fill="#555"/><circle cx="11" cy="8" r="2.6" fill="#fff"/></svg>
  <p class="abs footer-line" style="top:2096px">KAV Electric, llc.<br>18 Larkspur Ave<br>Millbrook, New Jersey 07000</p>

  <div class="abs social" style="left:796px"></div>
  <div class="abs social" style="left:837px"></div>
  <div class="abs social" style="left:879px"></div>
  <p class="abs copyright">© 2017 Brightline Today.</p>

</div>
</body>
</html>
```